Business Card Design Project

Please see logo design project "Medical Corporate Logo"

We are a small incorporated medical service in Australia with two staff currently serving contract work at a variety of clinics and eventually seeking to expand our services to a private clinic. Our work is based around emergency and general practice medical services.

Our name is Corlett Medical Services PTY LTD. We need a logo that is clean & modern, preferably black/white/grey but conveys a sense of familiarity, serenity, comfort and security conducive to medical practice. We have in mind a stylized or line drawing of Bertolani's sketch 'Lamp on a Ledge'.

We are also seeking matching business cards incorporating this logo for our staff.

Target Market(s)

Medical clinics, emergency departments, administrative staff, staffing agencies, patients

Industry/Entity Type

Security

Font styles to use
Serif

Requirements
Must have
• Our company name "Corlett Medical Services Pty Ltd"

Our staff names, qualifications and contact details
Dr Simon Trelawne
BNg BMBS (Tarrowby)
Trel0871@tarrowby.edu.au
0412 738406

Lorelle Trelawne
BNg (Tarrowby)
Clinical Governance Nurse
Trel0871@tarrowby.edu.au
0418 264937
Should not have
• Excessive decorations or complications. Simple borders or graphics are ok, but we would prefer them to be clean.

```html
<!DOCTYPE html>
<html lang="en">
<head>
<meta charset="utf-8">
<title>Corlett Medical Services – Business Cards</title>
<link href="https://fonts.googleapis.com/css2?family=Sorts+Mill+Goudy&family=Source+Sans+3:wght@400&display=swap" rel="stylesheet">
<style>
  :root {
    --paper: #ffffff;
    --trim: #c9c9c9;
    --crop: #7a7a7a;
    --ink: #3a3a3a;
    --ink-soft: #5a5a5a;
    --mark: #8f8f8f;
    --note: #1e1e1e;
  }
  html, body {
    margin: 0;
    padding: 0;
    width: 1200px;
    height: 901px;
    overflow: hidden;
    background: var(--paper);
  }
  .sheet {
    position: relative;
    width: 1200px;
    height: 901px;
    font-family: "Sorts Mill Goudy", Georgia, serif;
    color: var(--ink);
  }
  .crop-marks {
    position: absolute;
    inset: 0;
  }
  .card {
    position: absolute;
    left: 129px;
    width: 462px;
    box-sizing: border-box;
    border: 1px solid var(--trim);
    background: var(--paper);
    text-align: center;
  }
  .card--front { top: 105px; height: 283px; }
  .card--back  { top: 499px; height: 282px; }

  .brand { position: absolute; left: 0; right: 0; }
  .brand-seal {
    display: block;
    margin: 0 auto;
    border-radius: 50%;
    background: radial-gradient(circle at 45% 40%, #d8d8d8, #9a9a9a);
  }
  .brand-name {
    margin: 0;
    color: var(--ink);
    font-weight: 400;
    text-transform: uppercase;
    line-height: 1;
  }
  .card--front .brand { top: 62px; }
  .card--front .brand-seal { width: 66px; height: 66px; }
  .card--front .brand-name { margin-top: 36px; font-size: 38px; letter-spacing: 1px; }
  .card--front .brand-sub { margin-top: 8px; font-size: 14px; letter-spacing: 0.5px; }

  .card--back .brand { top: 24px; }
  .card--back .brand-seal { width: 42px; height: 42px; }
  .card--back .brand-name { margin-top: 22px; font-size: 23px; letter-spacing: 0.5px; }
  .card--back .brand-sub { margin-top: 5px; font-size: 9px; }

  .person {
    position: absolute;
    top: 149px;
    left: 0;
    right: 0;
  }
  .person-name { margin: 0; font-size: 20px; font-weight: 400; color: var(--ink-soft); letter-spacing: 0.3px; }
  .person-role,
  .person-qual { margin: 3px 0 0; font-size: 12.5px; color: var(--ink-soft); }

  .divider {
    position: absolute;
    top: 230px;
    left: 82px;
    width: 300px;
    height: 2px;
    background: linear-gradient(90deg, transparent, #8a8a8a 30%, #8a8a8a 70%, transparent);
  }
  .contact {
    position: absolute;
    top: 238px;
    left: 0;
    right: 0;
    margin: 0;
    font-size: 13px;
    color: var(--ink-soft);
  }
  .contact-label { color: var(--ink); font-weight: 400; margin-right: 3px; }
  .contact-item + .contact-item { margin-left: 8px; }

  .spec-note {
    position: absolute;
    left: 632px;
    top: 680px;
    margin: 0;
    font-family: "Source Sans 3", Arial, sans-serif;
    font-size: 24px;
    line-height: 33px;
    color: var(--note);
  }
</style>
</head>
<body>
<main class="sheet">
  <svg class="crop-marks" width="1200" height="901" aria-hidden="true">
    <g stroke="var(--crop)" stroke-width="1">
      <line x1="129.5" y1="70" x2="129.5" y2="95"/>
      <line x1="595.5" y1="70" x2="595.5" y2="95"/>
      <line x1="129.5" y1="403" x2="129.5" y2="430"/>
      <line x1="595.5" y1="403" x2="595.5" y2="430"/>
      <line x1="91" y1="105.5" x2="118" y2="105.5"/>
      <line x1="607" y1="105.5" x2="633" y2="105.5"/>
      <line x1="91" y1="392.5" x2="118" y2="392.5"/>
      <line x1="607" y1="392.5" x2="633" y2="392.5"/>

      <line x1="131.5" y1="462" x2="131.5" y2="487"/>
      <line x1="588.5" y1="462" x2="588.5" y2="487"/>
      <line x1="131.5" y1="791" x2="131.5" y2="816"/>
      <line x1="588.5" y1="791" x2="588.5" y2="816"/>
      <line x1="94" y1="497.5" x2="121" y2="497.5"/>
      <line x1="599" y1="497.5" x2="626" y2="497.5"/>
      <line x1="94" y1="777.5" x2="121" y2="777.5"/>
      <line x1="599" y1="777.5" x2="626" y2="777.5"/>
    </g>
  </svg>

  <section class="card card--front" aria-label="Card front">
    <div class="brand">
      <span class="brand-seal" role="img" aria-label="Company emblem"></span>
      <p class="brand-name">Corlett</p>
      <p class="brand-name brand-sub">Medical Services PTY LTD</p>
    </div>
  </section>

  <section class="card card--back" aria-label="Card back">
    <div class="brand">
      <span class="brand-seal" role="img" aria-label="Company emblem"></span>
      <p class="brand-name">Corlett</p>
      <p class="brand-name brand-sub">Medical Services PTY LTD</p>
    </div>
    <div class="person">
      <h2 class="person-name">Lorelle Trelawne</h2>
      <p class="person-role">Clinical Governance Nurse</p>
      <p class="person-qual">BNg (Tarrowby)</p>
    </div>
    <div class="divider"></div>
    <p class="contact">
      <span class="contact-item"><span class="contact-label">Phone</span>0418 264 937</span>
      <span class="contact-item"><span class="contact-label">Email</span>Trel0871@tarrowby.edu.au</span>
    </p>
  </section>

  <p class="spec-note">Double sided Business cards 90mm x 55mm<br>contact centred indented</p>
</main>
</body>
</html>
```